Norvane Builders Business Card

Modern and Professional Business Card for a Med size construction/development company.

See the samples below for the design I like … but I need ideas for incorporating the red company logo while still keeping the clean look of the card samples that are attached.

Logo and tag line on the back … info on the front.

Tagline: Quality Starts from the Ground Up

Target Market(s)

Med-Large General Contractors

Contact Information for Business Card

Norvane Builders Limited
42 Brenton Street
Elk Harbour, NL
B3K 7T2

t: 709-555-0147
f: 709-555-0192
w: www.norvanebuilders-example.com

Font styles to use
Sans Serif

Colors
fbee3e

Requirements
Must have
• I like the black and yellow designs of the attached samples …. but I'm not sure how to incorporate the red Norvane Builders logo into that design??
Nice to have
• Construction safety strips

```html
<!DOCTYPE html>
<html lang="en">
<head>
<meta charset="utf-8">
<title>Norvane Builders – Business Card</title>
<link rel="stylesheet" href="https://fonts.googleapis.com/css2?family=Montserrat:wght@700&family=Questrial&display=swap">
<style>
  :root {
    --stage: #3a3d42;
    --card: #070709;
    --brand-red: #ed1c24;
    --safety-yellow: #fbee3e;
    --text-light: #f4f4f4;
    --text-dark: #0b0b0b;
  }
  * { box-sizing: border-box; margin: 0; padding: 0; }
  html, body {
    width: 1200px; height: 1000px; overflow: hidden;
    background: var(--stage);
  }
  .stage {
    position: relative; width: 1200px; height: 1000px;
    display: flex; flex-direction: column; align-items: center; justify-content: center; gap: 64px;
  }
  .card {
    position: relative; width: 640px; height: 366px;
    background: var(--card); border-radius: 18px; overflow: hidden;
    box-shadow: 0 18px 40px rgba(0,0,0,.45);
    font-family: "Questrial", sans-serif; color: var(--text-light);
  }
  /* Back: name and tagline */
  .card--back { display: flex; flex-direction: column; align-items: center; justify-content: center; gap: 26px; }
  .brand-name {
    display: flex; align-items: center; gap: 12px;
    font-family: "Montserrat", sans-serif; font-weight: 700; color: var(--text-light);
    letter-spacing: .5px;
  }
  .brand-name__mark { width: 22px; height: 22px; background: var(--brand-red); }
  .card--back .brand-name { font-size: 34px; }
  .card--back .brand-name__mark { width: 30px; height: 30px; }
  .tagline { font-size: 17px; letter-spacing: .8px; }

  /* Front: contact details */
  .card--front .brand-name { position: absolute; left: 40px; top: 44px; font-size: 24px; }
  .contact {
    position: absolute; left: 40px; top: 150px;
    font-size: 16px; line-height: 1.35; list-style: none;
  }
  .contact__address { margin-bottom: 8px; }
  .contact__row { display: flex; align-items: center; gap: 10px; }
  .contact__icon { width: 14px; height: 14px; flex: none; fill: var(--safety-yellow); }
  .contact__accent { color: var(--safety-yellow); }
  .ribbon {
    position: absolute; right: 0; top: 118px; width: 355px; height: 62px;
    background: var(--safety-yellow);
    clip-path: polygon(0 10%, 22% 0, 100% 0, 100% 100%, 22% 100%);
    display: flex; align-items: center; justify-content: flex-end; padding-right: 24px;
    font-family: "Montserrat", sans-serif; font-weight: 700; font-size: 19px; color: var(--text-dark);
  }
</style>
</head>
<body>
<main class="stage">
  <section class="card card--back" aria-label="Card back">
    <div class="brand-name"><span class="brand-name__mark"></span>Norvane Builders Limited</div>
    <p class="tagline">Quality Starts from the Ground Up</p>
  </section>

  <section class="card card--front" aria-label="Card front">
    <div class="brand-name"><span class="brand-name__mark"></span>Norvane Builders Limited</div>
    <ul class="contact">
      <li class="contact__address">42 Brenton Street<br>Elk Harbour, NL B3K 7T2</li>
      <li class="contact__row">
        <svg class="contact__icon" viewBox="0 0 16 16" aria-hidden="true"><path d="M3 1l3 3-1.5 2a9 9 0 0 0 5.5 5.5L12 10l3 3-2 2C7 15 1 9 1 3z"/></svg>
        709-555-0147
      </li>
      <li class="contact__row">
        <svg class="contact__icon" viewBox="0 0 16 16" aria-hidden="true"><path d="M4 1h8v4H4zM1 6h14v6h-3v3H4v-3H1zm4 4v4h6v-4z"/></svg>
        709-555-0192
      </li>
      <li class="contact__row">
        <svg class="contact__icon" viewBox="0 0 16 16" aria-hidden="true"><path d="M1 3h14v10H1zm1.5 1.5v.3L8 9l5.5-4.2v-.3zM2.5 6.6v5h11v-5L8 10.8z"/></svg>
        info@norvanebuilders-example.com
      </li>
      <li class="contact__row">
        <svg class="contact__icon" viewBox="0 0 16 16" aria-hidden="true"><path d="M8 1a7 7 0 1 0 0 14A7 7 0 0 0 8 1zm-1 2.2c-.6 1-1.5 1.3-2.2 2.3.4 1 1.8 1 2.2 2 .3 1-.4 2.3.3 3.5l-1.5 1.8A5.6 5.6 0 0 1 7 3.2zm2.5.3a5.6 5.6 0 0 1 3.6 6.5c-.9-.6-1.5-1.7-2.6-1.6-1 .1-1.7-1-1.1-1.9.6-1 .3-2 .1-3z"/></svg>
        <span>www.<span class="contact__accent">norvanebuilders-example</span>.com</span>
      </li>
    </ul>
    <div class="ribbon">Norvane Builders Limited</div>
  </section>
</main>
</body>
</html>
```